brell carpentry & property maintenance

busines card for my carpentry business
easy to read
not to bogged out with to much info
I like the colour bule baby blue ish
repair it build it fix it
all aspects of carpentry and joinery
building work no job to small

Reason: I can not seem to get my logo to you guys could I have an email address please to send to thanks owen

Target Market(s)

home owners unit blocks people to busy to look after yard

Industry/Entity Type

Property Maintenance

Contact Information for Business Card

email: brellcarpentry@mailvane.com.au
phone 0427351846
Owen Brell qualified carpenter

Logo Text

brell carpentry $ property mainteaince

Logo styles of interest
Lettermark Logo
Requirements
Must have
• thinking logo front and back a blue print type sketch plans over card
would like logo to have B W like the one that I have on my file
I can not get the look n feel tool bare to work but it should be pointing more to the pro bold up market theme
my lic no 473152c
my name Owen Brell qualified carpenter
fully insured
Nice to have
• front int BW with Brell carpentry & property maintenance written through

```html
<!DOCTYPE html>
<html lang="en">
<head>
<meta charset="utf-8">
<title>Brell Carpentry &amp; Property Maintenance — Business Card</title>
<link rel="stylesheet" href="https://fonts.googleapis.com/css2?family=Raleway:wght@500;600;700&display=swap">
<style>
  :root {
    --page-bg: #e9e7e3;
    --card-blue: #2d4fb8;
    --card-blue-deep: #1c3590;
    --card-blue-light: #5f86dd;
    --band: rgba(20, 34, 90, 0.38);
    --ink-white: #ffffff;
    --ink-dark: #0e1430;
  }
  * { margin: 0; padding: 0; box-sizing: border-box; }
  html, body {
    width: 1200px; height: 785px; overflow: hidden;
    background: var(--page-bg);
    font-family: "Raleway", Arial, sans-serif;
  }
  .canvas {
    position: relative; width: 1200px; height: 785px;
    display: flex; align-items: center; justify-content: center;
  }
  .business-card {
    position: relative; width: 1040px; height: 620px; overflow: hidden;
    border-radius: 6px;
    box-shadow: 0 10px 30px rgba(0,0,0,0.25);
  }
  .blueprint-sketch {
    position: absolute; inset: 0;
    background:
      radial-gradient(ellipse at 45% 40%, var(--card-blue-light) 0%, transparent 55%),
      linear-gradient(135deg, var(--card-blue) 0%, var(--card-blue-deep) 100%);
  }
  .contact-band {
    position: absolute; left: 0; right: 0; top: 248px; height: 162px;
    background: var(--band);
  }
  .brand-mark {
    position: absolute; left: 430px; top: 48px;
    display: flex; align-items: center; gap: 22px;
  }
  .brand-square {
    width: 96px; height: 96px; background: var(--ink-white);
    border: 8px solid var(--ink-dark);
  }
  .brand-name {
    color: var(--ink-dark); font-weight: 700; font-size: 34px; line-height: 1.1;
    width: 440px;
  }
  .trade-name {
    position: absolute; left: 90px; top: 182px;
    color: var(--ink-white); font-weight: 700; font-size: 42px;
  }
  .contact-list {
    position: absolute; left: 560px; top: 262px;
    color: var(--ink-white); font-weight: 600; font-size: 26px; line-height: 1.45;
    list-style: none;
  }
  .owner {
    position: absolute; left: 90px; top: 272px; color: var(--ink-dark);
  }
  .owner-name { font-weight: 700; font-size: 34px; }
  .owner-role { font-weight: 600; font-size: 28px; margin-top: 8px; }
  .owner-licence { font-weight: 600; font-size: 19px; margin-top: 4px; }
  .tagline {
    position: absolute; color: var(--ink-dark); font-weight: 500;
  }
  .tagline-fix { left: 900px; top: 302px; font-size: 22px; }
  .tagline-build { left: 560px; top: 428px; font-size: 30px; }
  .tagline-repair { left: 90px; top: 520px; font-size: 34px; }
</style>
</head>
<body>
<main class="canvas">
  <section class="business-card" aria-label="Business card">
    <div class="blueprint-sketch" role="img" aria-label="Blueprint-style sketch of house plans in white lines over blue"></div>
    <div class="contact-band"></div>

    <div class="brand-mark">
      <div class="brand-square"></div>
      <p class="brand-name">Brell carpentry &amp; property maintenance</p>
    </div>

    <p class="trade-name">Brell carpentry</p>

    <ul class="contact-list">
      <li>brellcarpentry@mailvane.com.au</li>
      <li>0427351846</li>
    </ul>

    <div class="owner">
      <p class="owner-name">Owen Brell</p>
      <p class="owner-role">qualified carpenter</p>
      <p class="owner-licence">lic no 473152c</p>
    </div>

    <p class="tagline tagline-fix">fix it</p>
    <p class="tagline tagline-build">build it</p>
    <p class="tagline tagline-repair">Repair it</p>
  </section>
</main>
</body>
</html>
```